Clear Plastic Card Design

I am looking to have a business card designed from my logo icon. I am looking to match the style of a different business card I have attached in the files.
Looking for a card that is plastic, with layers of transparency in the shape of my logo icon (also attached in the files) - not a circle like the other card. The winning design will incorporate the red icon logo on the front and back and include the charity's name, "Lanterns for the Weary" in the same or similar font, as well as an email and phone number. For now, use the email: email@lanternsfortheweary.org and the phone number 555-318-4072.
We like how the sample business card has transparency, partial and full opacity layers and a matching color scheme. Files will need to be in vector so that our business card printing company can work with it.
UPDATE:
We've some excellent designs in, thank you everyone! I got an early review from the owner, and he requested a minor redirect to find his perfect design. He wants the design to stand out by NOT being a rectangle. Try instead a circle, square, or best yet - something that falls in the outline of the logo icon, either fully or partially. Thank you, everyone!
Contact Information for Business Card
Lanterns for the Weary text should be incorporated as well as a phone and email.
Look and feel

```html
<!DOCTYPE html>
<html lang="en">
<head>
<meta charset="utf-8">
<title>Lanterns for the Weary – Business Card</title>
<link rel="stylesheet" href="https://fonts.googleapis.com/css2?family=Arimo:wght@400;700&display=swap">
<style>
  :root {
    --page-bg: #ece9e6;
    --red-deep: #a90f14;
    --red-main: #cc1b1f;
    --red-soft: #e04a46;
    --frost: rgba(255, 255, 255, 0.88);
    --ink-dark: #3a3a3a;
    --ink-light: #ffffff;
  }
  html, body {
    margin: 0;
    width: 1200px;
    height: 900px;
    overflow: hidden;
    background: var(--page-bg);
    font-family: "Arimo", Arial, sans-serif;
  }
  .business-card {
    position: absolute;
    left: 170px;
    top: 194px;
    width: 860px;
    height: 513px;
  }
  .card-shape {
    position: absolute;
    inset: 0;
    width: 860px;
    height: 513px;
    overflow: visible;
  }
  .org-name {
    position: absolute;
    left: 120px;
    top: 225px;
    width: 340px;
    margin: 0;
    text-align: center;
    font-size: 30px;
    font-weight: 400;
    line-height: 1.25;
    color: var(--ink-dark);
  }
  .contact-block {
    position: absolute;
    right: 65px;
    top: 295px;
    text-align: right;
    color: var(--ink-light);
  }
  .person-name {
    margin: 0;
    font-size: 31px;
    font-weight: 700;
    letter-spacing: 0.5px;
  }
  .person-title {
    margin: 6px 0 0;
    font-size: 20px;
  }
  .contact-list {
    list-style: none;
    margin: 24px 0 0;
    padding: 0;
    font-size: 19px;
  }
  .contact-list li {
    display: flex;
    justify-content: flex-end;
    align-items: center;
    gap: 12px;
    height: 31px;
  }
  .contact-icon {
    width: 16px;
    height: 16px;
    flex: none;
  }
  .contact-list .web-line { padding-right: 28px; }
</style>
</head>
<body>
  <div class="business-card">
    <svg class="card-shape" viewBox="0 0 860 513" aria-hidden="true">
      <defs>
        <linearGradient id="cardRed" x1="0" y1="0" x2="1" y2="0.4">
          <stop offset="0" stop-color="var(--red-soft)"/>
          <stop offset="0.45" stop-color="var(--red-main)"/>
          <stop offset="1" stop-color="var(--red-deep)"/>
        </linearGradient>
      </defs>
      <path d="M118 0 H846 a14 14 0 0 1 14 14 V499 a14 14 0 0 1 -14 14 H290 A250 250 0 0 1 118 0 Z" fill="url(#cardRed)"/>
      <circle cx="290" cy="263" r="250" fill="url(#cardRed)"/>
      <circle cx="290" cy="263" r="222" fill="none" stroke="rgba(140,10,14,0.45)" stroke-width="10"/>
      <circle cx="290" cy="263" r="208" fill="var(--frost)"/>
    </svg>

    <p class="org-name">Lanterns for<br>the Weary</p>

    <div class="contact-block">
      <h1 class="person-name">MARCUS HALE</h1>
      <p class="person-title">Founder &amp; CEO</p>
      <ul class="contact-list">
        <li>555-318-4072
          <svg class="contact-icon" viewBox="0 0 16 16" aria-hidden="true"><path d="M4 1.5 L6.2 4.6 5 6.1 C6 8.2 7.8 10 9.9 11 L11.4 9.8 14.5 12 13.4 14.2 C8 14.6 1.4 8 1.8 2.6 Z" fill="#fff"/></svg>
        </li>
        <li>info@lanternsfortheweary.org
          <svg class="contact-icon" viewBox="0 0 16 16" aria-hidden="true"><rect x="1.5" y="3.5" width="13" height="9" fill="#fff"/><path d="M1.5 3.5 L8 9 14.5 3.5" fill="none" stroke="#c0161a" stroke-width="1.2"/></svg>
        </li>
        <li class="web-line">lanternsfortheweary.org</li>
      </ul>
    </div>
  </div>
</body>
</html>
```